Healthcare food company need product packaging design

We need a food supplements product packaging design for an all natural wholesome food.
For natural wholesome design, we need a fresh and clean looking label as the products contain soybean, kale and broccoli as an alternative protein food powder. To appeal to the health conscious consumer .

Target Market(s)

For natural wholesome food, all age group

Industry/Entity Type

Health And Wellness

Font styles to use
Serif
Sans Serif

Requirements
Must have
• Strong colours and bigger font size to attract consumer when product is placed on shelf
Nice to have
• Fresh vegetable colours with elements of green or mutiple colours
Should not have
• No restriction

```html
<!DOCTYPE html>
<html lang="en">
<head>
<meta charset="utf-8">
<title>LeafLea – All Plant Source Protein Powder Label</title>
<link href="https://fonts.googleapis.com/css2?family=Roboto+Condensed:wght@300;400&family=Open+Sans:wght@400&display=swap" rel="stylesheet">
<style>
  :root {
    --backdrop: #6b7522;
    --label-white: #ffffff;
    --brand-green: #7fa33a;
    --soft-green: #9cc24a;
    --light-green: #c4dc7a;
    --pale-green: #e4efc0;
    --deep-green: #5f8c22;
    --rule-grey: #b9b9b9;
    --tag-grey: #8a8a8a;
  }
  * { margin: 0; padding: 0; box-sizing: border-box; }
  html, body { width: 800px; height: 1200px; overflow: hidden; }
  body {
    background: var(--backdrop);
    position: relative;
    font-family: "Roboto Condensed", sans-serif;
  }
  .label {
    position: absolute;
    left: 170px;
    top: 290px;
    width: 460px;
    height: 620px;
    background: var(--label-white);
    overflow: hidden;
  }
  .label__waves {
    position: absolute;
    inset: 0;
  }
  .brand {
    position: absolute;
    top: 108px;
    left: 0;
    width: 100%;
    display: flex;
    justify-content: center;
    align-items: center;
    gap: 10px;
  }
  .brand__name {
    font-family: "Roboto Condensed", sans-serif;
    font-weight: 300;
    font-size: 58px;
    color: var(--brand-green);
    letter-spacing: 1px;
    line-height: 1;
  }
  .brand__dot {
    width: 16px;
    height: 16px;
    border-radius: 50%;
    background: var(--soft-green);
  }
  .tagline {
    position: absolute;
    top: 182px;
    left: 50px;
    right: 50px;
    display: flex;
    align-items: center;
    gap: 8px;
    font-family: "Open Sans", sans-serif;
    font-size: 13px;
    color: var(--tag-grey);
    white-space: nowrap;
  }
  .tagline::before, .tagline::after {
    content: "";
    flex: 1;
    height: 1px;
    background: var(--rule-grey);
  }
  .product-title {
    position: absolute;
    top: 250px;
    left: 0;
    width: 100%;
    text-align: center;
    font-weight: 400;
    font-size: 21px;
    color: var(--soft-green);
    letter-spacing: 0.2px;
  }
  .product-photo {
    position: absolute;
    left: 12px;
    top: 350px;
    width: 164px;
    height: 300px;
    border-radius: 50%;
    background: radial-gradient(ellipse at 45% 45%, #8fb550 0%, #5e8a2e 55%, #3f5f22 100%);
    border: 3px solid var(--label-white);
  }
</style>
</head>
<body>
  <section class="label">
    <svg class="label__waves" width="460" height="620" viewBox="0 0 460 620" aria-hidden="true">
      <path d="M0 560 C120 470 260 380 460 310 L460 620 L0 620 Z" fill="var(--pale-green)"/>
      <path d="M0 600 C150 520 300 440 460 350 L460 430 C330 500 200 560 60 620 L0 620 Z" fill="var(--soft-green)"/>
      <path d="M40 620 C190 560 320 500 460 440 L460 500 C350 540 260 580 170 620 Z" fill="var(--light-green)"/>
      <path d="M150 620 C260 580 360 540 460 520 L460 620 Z" fill="var(--brand-green)"/>
      <path d="M20 500 C160 420 300 360 460 300" stroke="var(--light-green)" stroke-width="3" fill="none"/>
      <path d="M200 610 C300 570 380 545 460 535" stroke="var(--label-white)" stroke-width="4" fill="none"/>
      <path d="M250 400 C330 330 400 290 460 250 L460 290 C400 320 330 360 250 400 Z" fill="var(--deep-green)" opacity="0.5"/>
    </svg>

    <div class="brand">
      <span class="brand__name">LeafLea</span>
      <span class="brand__dot"></span>
    </div>
    <p class="tagline">Healty Food Healty Life</p>

    <h1 class="product-title">ALL PLANT SOURCE PROTEIN POWDER</h1>

    <div class="product-photo" role="img" aria-label="Photo of a green smoothie glass with celery, a green apple, a halved kiwi and a lime slice"></div>
  </section>
</body>
</html>
```